redesing professional certificate

Redesign our certificate to more a professional look and to make it look like a-wanna have - Best in adobe photoshop, because this template will be our basic, and we have in our education different levels, basic, upper, lower, complex, master level. I usually add a small picture to show what level they are. Or when you have a better suggestion I a gladly to hear.
We teach to physiotherapist so it has to look professional.

Target Market(s)

physiotherapist

Industry/Entity Type

Health Care

Requirements
Must have
• our logo

```html
<!DOCTYPE html>
<html lang="en">
<head>
<meta charset="utf-8">
<title>Level 1 Certificate</title>
<link rel="stylesheet" href="https://fonts.googleapis.com/css2?family=Bebas+Neue&family=Manrope:wght@400;500;700;800&display=swap">
<style>
  :root {
    --navy: #10283f;
    --orange: #f39322;
    --yellow: #facd1f;
    --pale: #f6eba6;
    --gold: #fbbf1e;
    --badge: #b98a3e;
    --paper: #ffffff;
    --backdrop: #e4e4e4;
  }
  html, body {
    margin: 0;
    width: 1200px;
    height: 1200px;
    overflow: hidden;
    background: var(--backdrop);
  }
  .certificate {
    position: absolute;
    left: 175px;
    top: 0;
    width: 887px;
    height: 1252px;
    background: var(--paper);
    transform: scale(0.9585);
    transform-origin: top left;
    overflow: hidden;
    font-family: "Manrope", sans-serif;
    color: var(--navy);
  }
  .certificate__art {
    position: absolute;
    inset: 0;
  }
  .brand {
    position: absolute;
    left: 475px;
    top: 123px;
    transform: translate(-50%, -50%);
    display: flex;
    align-items: center;
    gap: 12px;
  }
  .brand__dot {
    width: 34px;
    height: 34px;
    border-radius: 50%;
    background: var(--navy);
  }
  .brand__name {
    font-size: 40px;
    font-weight: 800;
    color: var(--navy);
  }
  .level-badge {
    position: absolute;
    left: 685px;
    top: 68px;
    width: 140px;
    height: 140px;
    border-radius: 50%;
    background: radial-gradient(circle at 40% 35%, #e9c57a, var(--badge) 60%, #7a5620);
  }
  .title {
    position: absolute;
    left: 0;
    right: 0;
    top: 258px;
    margin: 0;
    padding-left: 175px;
    text-align: center;
    font-family: "Bebas Neue", sans-serif;
    font-weight: 400;
    font-size: 98px;
    line-height: 1;
    color: var(--navy);
  }
  .block {
    position: absolute;
    left: 175px;
    right: 0;
    text-align: center;
    margin: 0;
  }
  .recipient {
    top: 412px;
    font-size: 36px;
    font-weight: 700;
  }
  .course {
    top: 467px;
    font-size: 24px;
    line-height: 32px;
    font-weight: 500;
  }
  .course strong { font-weight: 800; }
  .signatory {
    position: absolute;
    top: 790px;
    width: 300px;
    transform: translateX(-50%);
    text-align: center;
    font-size: 22px;
    line-height: 28px;
  }
  .signatory--left { left: 310px; }
  .signatory--right { left: 648px; }
  .signatory__name { font-weight: 700; display: block; }
  .registration {
    top: 917px;
    font-size: 22px;
    font-weight: 500;
  }
  .terms {
    top: 960px;
    font-size: 21px;
    line-height: 27px;
    font-weight: 500;
  }
  .issuer {
    top: 1136px;
    font-size: 24px;
    font-weight: 800;
    line-height: 30px;
  }
  .issuer__address {
    display: block;
    font-size: 17px;
    font-weight: 500;
    line-height: 20px;
  }
  .issuer__tagline {
    display: block;
    margin-top: 12px;
    font-size: 21px;
    font-weight: 800;
  }
</style>
</head>
<body>
<main class="certificate">
  <svg class="certificate__art" viewBox="0 0 887 1252" width="887" height="1252" aria-hidden="true">
    <defs>
      <linearGradient id="footer-glow" x1="0" y1="0" x2="1" y2="0">
        <stop offset="0" stop-color="#f7efb4"/>
        <stop offset="0.55" stop-color="#f9d968"/>
        <stop offset="1" stop-color="#fbbe1e"/>
      </linearGradient>
    </defs>
    <path class="footer-wave" fill="url(#footer-glow)" d="M100,1252 L100,1140 C450,1135 700,1090 887,1025 L887,1252 Z"/>
    <path class="wave-orange" fill="var(--orange)" d="M0,0 L165,0 C100,120 60,260 55,420 C50,600 130,800 170,900 C200,1000 195,1150 140,1252 L0,1252 Z"/>
    <path class="wave-yellow" fill="var(--yellow)" d="M108,0 L240,0 C140,90 80,230 72,400 C65,560 130,700 158,850 C175,950 168,1050 118,1130 L60,1252 L0,1252 L0,0 Z"/>
    <path class="wave-navy" fill="var(--navy)" d="M0,0 L108,0 C55,150 20,300 22,440 C25,600 95,720 112,860 C125,980 138,1080 110,1150 C90,1200 72,1230 55,1252 L0,1252 Z"/>
    <path class="wave-corner" fill="var(--yellow)" d="M0,1195 C35,1180 65,1150 92,1112 L100,1128 C72,1188 45,1228 28,1252 L0,1252 Z"/>
  </svg>

  <div class="brand">
    <span class="brand__dot"></span>
    <span class="brand__name">Kinetra</span>
  </div>
  <div class="level-badge" role="img" aria-label="Level badge"></div>

  <h1 class="title">CERTIFICATE</h1>

  <p class="block recipient">Lucas Moreno</p>
  <p class="block course">
    Has completed the fasciatherapy <strong>level 1</strong> course.<br>
    - 3 days, 15 -17 February 2020 -<br>
    Kopavogur, Iceland 17 February 2020
  </p>

  <div class="signatory signatory--left">
    <span class="signatory__name">Mr. JB van Dalen</span>
    Co-Director
  </div>
  <div class="signatory signatory--right">
    <span class="signatory__name">Mr. RT Osman</span>
    Co-Director
  </div>

  <p class="block registration">Registration number: 1 ICE 20</p>
  <p class="block terms">
    The Kinetra Method ongoing certification<br>
    is contingent upon meeting the requirements of the<br>
    maintenance of the certification of Fasciatherapy.
  </p>

  <p class="block issuer">
    Myoflow BV
    <span class="issuer__address">Lindengracht 48, 1015KK Amsterdam, The Netherlands</span>
    <span class="issuer__tagline">Specialist in fasciatherapy innovation</span>
  </p>
</main>
</body>
</html>
```